Presentation Folder

We want to create a clean, modern folder for our three companies- A single folder. Feel free to be as creative as possible. We are good with some color, but want it to stay clean and modern. See our website veltrimhire.net for more idea of the vibe. I've attached all 3 logos to be used as well as our new business cards

Target Market(s)

Senior executives

Industry/Entity Type

Business

Font styles to use
Serif
Sans Serif

Colors
85acd3
3176b5
0455a3
0792cd
34a6d7
85cae6

Requirements
Must have
• All 3 logos websites and phone numbers (see business card).

```html
<!DOCTYPE html>
<html lang="en">
<head>
<meta charset="utf-8">
<title>Presentation Folder – Outside</title>
<link href="https://fonts.googleapis.com/css2?family=Montserrat:wght@500;600&family=Open+Sans:wght@400&display=swap" rel="stylesheet">
<style>
  :root {
    --stage: #4b4b4b;
    --sky: #85cae6;
    --sky-deep: #7cc2e2;
    --paper: #ffffff;
    --navy: #1d4e8f;
    --slate: #5b5d66;
    --rule: #6d6d6d;
    --ink: #444444;
    --icon: #3176b5;
  }
  * { margin: 0; padding: 0; box-sizing: border-box; }
  html, body { width: 1200px; height: 1000px; overflow: hidden; }
  body { background: var(--stage); position: relative; font-family: "Open Sans", Arial, sans-serif; }

  .folder {
    position: absolute; left: 42px; top: 68px; width: 1116px; height: 744px;
    background: var(--paper);
  }
  .folder__art {
    position: absolute; left: 0; top: 0; width: 1116px; height: 588px;
    background:
      radial-gradient(ellipse 520px 140px at 640px 400px, rgba(255,255,255,0.35), rgba(255,255,255,0) 70%),
      radial-gradient(ellipse 160px 420px at 60px 360px, rgba(255,255,255,0.22), rgba(255,255,255,0) 70%),
      radial-gradient(ellipse 220px 160px at 1030px 110px, rgba(255,255,255,0.28), rgba(255,255,255,0) 70%),
      linear-gradient(180deg, var(--sky) 0%, var(--sky-deep) 100%);
  }
  .folder__band { position: absolute; left: 0; top: 588px; width: 1116px; height: 156px; }

  .rule { position: absolute; background: var(--rule); }
  .rule--v { width: 1px; }
  .rule--h { height: 1px; }

  .brand {
    position: absolute; display: flex; align-items: center; gap: 8px;
    font-family: "Montserrat", Arial, sans-serif; font-weight: 600; white-space: nowrap;
  }
  .brand__mark { display: inline-block; flex: none; }
  .brand--academy { color: var(--navy); }
  .brand--corvane { color: var(--slate); }
  .brand--veltrim { color: var(--navy); }
  .brand--academy .brand__mark { background: var(--navy); }
  .brand--corvane .brand__mark { background: var(--slate); }
  .brand--veltrim .brand__mark { background: var(--navy); border-radius: 50%; }

  .contact {
    position: absolute; font-size: 7px; line-height: 12px; color: var(--ink);
    display: flex; flex-direction: column;
  }
  .contact__row { display: flex; align-items: center; gap: 4px; }
  .contact--right { align-items: flex-end; }
  .contact svg { width: 7px; height: 9px; flex: none; }
</style>
</head>
<body>
  <section class="folder">
    <div class="folder__art" role="img" aria-label="Fine white line-wave ribbon flowing across a light blue field"></div>

    <div class="folder__band">
      <!-- Back panel -->
      <div class="brand brand--academy" style="left:50px; top:40px; font-size:11px; flex-direction:column; gap:4px; align-items:center; width:80px;">
        <span class="brand__mark" style="width:9px;height:9px;"></span>
        <span>THE LUMEN<br>ACADEMY</span>
      </div>
      <div class="contact" style="left:52px; top:96px;">
        <div class="contact__row">
          <svg viewBox="0 0 7 10"><rect x="1" y="0.5" width="5" height="9" rx="1" fill="none" stroke="var(--icon)"/></svg>877.555.0142
        </div>
        <div class="contact__row">
          <svg viewBox="0 0 10 10"><circle cx="5" cy="5" r="4.3" fill="none" stroke="var(--icon)"/><path d="M1 5h8M5 1v8" stroke="var(--icon)" stroke-width="0.8"/></svg>lumenacademy.com
        </div>
      </div>

      <div class="rule rule--v" style="left:171px; top:36px; height:86px;"></div>
      <div class="rule rule--h" style="left:171px; top:78px; width:342px;"></div>

      <div class="contact contact--right" style="right:834px; top:34px;">
        <div class="contact__row">800.555.0178<svg viewBox="0 0 7 10"><rect x="1" y="0.5" width="5" height="9" rx="1" fill="none" stroke="var(--icon)"/></svg></div>
        <div class="contact__row">CorvaneAssociates.com<svg viewBox="0 0 10 10"><circle cx="5" cy="5" r="4.3" fill="none" stroke="var(--icon)"/><path d="M1 5h8M5 1v8" stroke="var(--icon)" stroke-width="0.8"/></svg></div>
      </div>
      <div class="brand brand--corvane" style="left:300px; top:37px; font-size:12px;">
        <span class="brand__mark" style="width:22px;height:22px;"></span>CORVANE ASSOCIATES
      </div>

      <div class="contact contact--right" style="right:834px; top:94px;">
        <div class="contact__row">800.555.0193<svg viewBox="0 0 7 10"><rect x="1" y="0.5" width="5" height="9" rx="1" fill="none" stroke="var(--icon)"/></svg></div>
        <div class="contact__row">veltrimhire.net<svg viewBox="0 0 10 10"><circle cx="5" cy="5" r="4.3" fill="none" stroke="var(--icon)"/><path d="M1 5h8M5 1v8" stroke="var(--icon)" stroke-width="0.8"/></svg></div>
      </div>
      <div class="brand brand--veltrim" style="left:306px; top:94px; font-size:18px;">
        <span class="brand__mark" style="width:22px;height:22px;"></span>VELTRIM HIRE
      </div>

      <!-- Front panel -->
      <div class="brand brand--academy" style="left:618px; top:32px; font-size:19px; flex-direction:column; gap:6px; align-items:center; width:120px; text-align:center; line-height:1.25;">
        <span class="brand__mark" style="width:16px;height:16px;"></span>
        <span>THE LUMEN<br>ACADEMY</span>
      </div>

      <div class="rule rule--v" style="left:766px; top:36px; height:86px;"></div>
      <div class="rule rule--h" style="left:766px; top:79px; width:304px;"></div>

      <div class="brand brand--veltrim" style="left:808px; top:36px; font-size:18px;">
        <span class="brand__mark" style="width:22px;height:22px;"></span>VELTRIM HIRE
      </div>
      <div class="brand brand--corvane" style="left:808px; top:96px; font-size:12px;">
        <span class="brand__mark" style="width:22px;height:22px;"></span>CORVANE ASSOCIATES
      </div>
    </div>
  </section>
</body>
</html>
```